BUSINESS CARD MIRELLE KOSVIK

I need a new business card for my personal business.
I am a Naturopath and Nutritionist working doing private consults in the health and wellness arena.
I would like to see designs that are, clean minimalist but colourful.
I like:
White (clean,fresh, minimalist)
pops of one colour ONLY.Choose a colour to run with and keep it simple.
green
light blue
mustard
Bright yellow
Charcoal
The final design should communicate professionalism but also be in touch with nature.
Key Information to include:
MIRELLE KOSVIK
ABN 41 582 307 916
PTRQB 872310
Tel 0491 738 624
NATUROPATH | HERBALIST | NUTRITON CONSULTANT
BHSc (Naturopathic Studies) Grad Dip (Naturopathy)
BACK OF CARD : YOUR NEXT APPOINTMENT ..................................
I already have a logo (picture attached)But I would be more than happy to NOT have this included. I am very Open to cards WITHOUT current logo/ ones that weave the colour of my logo but do not use the logo.
I have included pictures attached to give examples of the styles/colors I enjoy.
Updates
I have added a picture of a mortar and pestle - one just like this would be lovely to include in your entry.
TIA

```html
<!DOCTYPE html>
<html lang="en">
<head>
<meta charset="utf-8">
<title>Mirelle Kosvik Naturopathy – Business Cards</title>
<link rel="stylesheet" href="https://fonts.googleapis.com/css2?family=Questrial&display=swap">
<style>
  :root {
    --lime: #b1cf3b;
    --white: #ffffff;
    --ink: #5a5a5a;
    --ink-soft: #666666;
    --leaf-grey: #9a9a9a;
    --stage: #ebe8e3;
  }
  * { margin: 0; padding: 0; box-sizing: border-box; }
  html, body {
    width: 1200px; height: 1000px; overflow: hidden;
    background: var(--stage);
    font-family: "Questrial", "Century Gothic", sans-serif;
  }
  .canvas { position: relative; width: 1200px; height: 1000px; }

  .card {
    position: absolute;
    width: 590px; height: 340px;
    border-radius: 28px;
    overflow: hidden;
    box-shadow: 0 4px 14px rgba(0,0,0,0.18);
  }
  .card--front { background: var(--lime); color: var(--white); }
  .card--back  { background: var(--white); color: var(--ink); }

  .front-name {
    position: absolute; right: 26px; top: 52px;
    font-size: 30px; letter-spacing: 0.5px; text-align: right;
  }
  .front-title {
    position: absolute; right: 26px; top: 96px;
    font-size: 23px; letter-spacing: 6px; text-align: right;
  }
  .front-ids {
    position: absolute; right: 46px; top: 266px;
    font-size: 13px; line-height: 17px; text-align: right;
  }

  .leaf-art { position: absolute; right: 0; top: 0; width: 590px; height: 340px; }

  .back-name {
    position: absolute; left: 28px; top: 56px;
    font-size: 23.5px; color: var(--ink); white-space: nowrap;
  }
  .back-name .accent { color: var(--lime); }
  .back-roles {
    position: absolute; left: 28px; top: 92px;
    font-size: 13.5px; line-height: 19px; color: var(--ink-soft); white-space: nowrap;
  }
  .back-contact {
    position: absolute; left: 27px; top: 266px;
    list-style: none; font-size: 15px; line-height: 19px; color: var(--ink);
  }
  .back-contact li { display: flex; align-items: center; gap: 4px; }
  .back-contact svg { width: 15px; height: 15px; flex: none; }
</style>
</head>
<body>
<main class="canvas">

  <!-- Row 1 -->
  <section class="card card--front" style="left:6px; top:155px;">
    <h1 class="front-name">MIRELLE KOSVIK</h1>
    <p class="front-title">NATUROPATHY</p>
    <p class="front-ids">ABN 41 582 307 916<br>PTRQB 872310</p>
  </section>

  <section class="card card--back" style="left:607px; top:155px;">
    <svg class="leaf-art" viewBox="0 0 590 340" role="img" aria-label="Skeleton leaf illustration in lime green">
      <defs>
        <radialGradient id="leafLime" cx="0.75" cy="0.6" r="0.6">
          <stop offset="0" stop-color="#b1cf3b" stop-opacity="0.75"/>
          <stop offset="1" stop-color="#b1cf3b" stop-opacity="0.25"/>
        </radialGradient>
      </defs>
      <ellipse cx="520" cy="210" rx="240" ry="190" transform="rotate(-38 520 210)" fill="url(#leafLime)"/>
    </svg>
    <h2 class="back-name">MIRELLE KOSVIK <span class="accent">NATUROPATH</span></h2>
    <p class="back-roles">NATUROPATH | HERBALIST | NUTRITON CONSULTANT<br>BHSc (Naturopathic Studies) Grad Dip (Naturopathy)</p>
    <ul class="back-contact">
      <li><svg viewBox="0 0 16 16"><circle cx="8" cy="8" r="7.5" fill="#b1cf3b"/><rect x="5.5" y="3.5" width="5" height="9" rx="1" fill="none" stroke="#fff" stroke-width="1.2"/></svg>0491 738 624</li>
      <li><svg viewBox="0 0 16 16"><circle cx="8" cy="8" r="7.5" fill="#b1cf3b"/><rect x="4" y="5" width="8" height="6" fill="none" stroke="#fff" stroke-width="1.1"/><path d="M4 5l4 3.5L12 5" fill="none" stroke="#fff" stroke-width="1.1"/></svg>mirellekosvik@leafpost.com</li>
    </ul>
  </section>

  <!-- Row 2 -->
  <section class="card card--front" style="left:4px; top:532px;">
    <h1 class="front-name">MIRELLE KOSVIK</h1>
    <p class="front-title">NATUROPATHY</p>
    <p class="front-ids">ABN 41 582 307 916<br>PTRQB 872310</p>
  </section>

  <section class="card card--back" style="left:605px; top:532px;">
    <svg class="leaf-art" viewBox="0 0 590 340" role="img" aria-label="Skeleton leaf illustration in soft grey">
      <defs>
        <radialGradient id="leafGrey" cx="0.75" cy="0.6" r="0.6">
          <stop offset="0" stop-color="#9a9a9a" stop-opacity="0.7"/>
          <stop offset="1" stop-color="#9a9a9a" stop-opacity="0.2"/>
        </radialGradient>
      </defs>
      <ellipse cx="520" cy="200" rx="240" ry="190" transform="rotate(-50 520 200)" fill="url(#leafGrey)"/>
    </svg>
    <h2 class="back-name">MIRELLE KOSVIK <span class="accent">NATUROPATH</span></h2>
    <p class="back-roles">NATUROPATH | HERBALIST | NUTRITON CONSULTANT<br>BHSc (Naturopathic Studies) Grad Dip (Naturopathy)</p>
    <ul class="back-contact">
      <li><svg viewBox="0 0 16 16"><circle cx="8" cy="8" r="7.5" fill="#b1cf3b"/><rect x="5.5" y="3.5" width="5" height="9" rx="1" fill="none" stroke="#fff" stroke-width="1.2"/></svg>0491 738 624</li>
      <li><svg viewBox="0 0 16 16"><circle cx="8" cy="8" r="7.5" fill="#b1cf3b"/><rect x="4" y="5" width="8" height="6" fill="none" stroke="#fff" stroke-width="1.1"/><path d="M4 5l4 3.5L12 5" fill="none" stroke="#fff" stroke-width="1.1"/></svg>mirellekosvik@leafpost.com</li>
    </ul>
  </section>

</main>
</body>
</html>
```